Business Card Design Project

This design is a slimline business card 45mm x90mm, the card will be printed at 49mm x 94mm and cut to 45mm x90 mm, this needs to be considered in the design. The content required on the front and back of the business card is attached in a pdf; the design will be done using photo shop as we use CS6 in our business. The design needs to be developed using a CMYK colour pallet, the main colours used on our business are red, grey black and white. A snapshot of our business brochure and new website has been provided to give you an understanding on our businesses look and feel.
FRONT OF BUSINESS CARD
Director
Marcus Feld
Ph+61 0421780213
www.brightvanecontracting.com.au
marcusfeld@brightvanecontracting.com.au
BACK OF BUSINESS CARD
SUPPORTING CLIENTS IN
Oil & Gas I Minerals & Metals I Petrochemical I Manufacturing
Building & Construction I Telecommunication I Rail I Civil I New Industries
KNOWLEDGE I EXPERTISE I EXPERIENCE I CAPACITY

```html
<!DOCTYPE html>
<html lang="en">
<head>
<meta charset="UTF-8">
<title>Business Card – Back</title>
<link href="https://fonts.googleapis.com/css2?family=Open+Sans:wght@700&display=swap" rel="stylesheet">
<style>
  :root {
    --card-black: #0a0a0a;
    --card-grey: #4a4a4a;
    --brand-red: #e3151c;
    --text-white: #ffffff;
  }
  html, body {
    margin: 0;
    padding: 0;
    overflow: hidden;
    background: var(--card-black);
  }
  .card-back {
    position: relative;
    width: 1200px;
    height: 625px;
    overflow: hidden;
    background: var(--card-black);
  }
  .card-texture {
    position: absolute;
    inset: 0;
    background: linear-gradient(100deg, var(--card-grey) 0%, #1c1c1c 35%, var(--card-black) 60%, #262626 100%);
  }
  .card-content {
    position: absolute;
    left: 0;
    right: 0;
    top: 190px;
    text-align: center;
    font-family: "Open Sans", "Myriad Pro", Arial, sans-serif;
    font-weight: 700;
    font-size: 31px;
    line-height: 43px;
    letter-spacing: -0.3px;
  }
  .sectors-heading,
  .capabilities {
    margin: 0;
    font: inherit;
    color: var(--brand-red);
  }
  .sector-list {
    margin: 0;
    color: var(--text-white);
  }
  .sector-list span {
    display: block;
    white-space: nowrap;
  }
  .capabilities { margin-top: 46px; }
</style>
</head>
<body>
  <div class="card-back">
    <div class="card-texture" role="img" aria-label="Dark grey textured background photograph"></div>
    <div class="card-content">
      <h2 class="sectors-heading">SUPPORTING CLIENTS IN</h2>
      <p class="sector-list">
        <span>Oil &amp; Gas | Minerals &amp; Metals | Petrochemical | Manufacturing |</span>
        <span>Building &amp; Construction | Telecommunication | Rail | Civil | New</span>
        <span>Industries</span>
      </p>
      <p class="capabilities">KNOWLEDGE | EXPERTISE | EXPERIENCE | CAPACITY</p>
    </div>
  </div>
</body>
</html>
```